Norvane Builders Business Card

Modern and Professional Business Card for a Med size construction/development company.

See the samples below for the design I like … but I need ideas for incorporating the red company logo while still keeping the clean look of the card samples that are attached.

Logo and tag line on the back … info on the front.

Tagline: Quality Starts from the Ground Up

Target Market(s)

Med-Large General Contractors

Contact Information for Business Card

Norvane Builders Limited
42 Brenton Street
Elk Harbour, NL
B3K 7T2

t: 709-555-0147
f: 709-555-0192
w: www.norvanebuilders-example.com

Font styles to use
Sans Serif

Colors
fbee3e

Requirements
Must have
• I like the black and yellow designs of the attached samples …. but I'm not sure how to incorporate the red Norvane Builders logo into that design??
Nice to have
• Construction safety strips

```html
<!DOCTYPE html>
<html lang="en">
<head>
<meta charset="utf-8">
<title>Norvane Builders Business Card</title>
<link href="https://fonts.googleapis.com/css2?family=Montserrat:wght@400;600;700&family=Oswald:wght@500&display=swap" rel="stylesheet">
<style>
  :root {
    --page: #2a2a2a;
    --card-black: #141414;
    --card-black-light: #262626;
    --brand-red: #e31e24;
    --brand-yellow: #fbee3e;
    --white: #ffffff;
    --text-grey: #b5b5b5;
  }
  * { margin: 0; padding: 0; box-sizing: border-box; }
  html, body { width: 1200px; height: 960px; overflow: hidden; }
  body {
    background: var(--page);
    font-family: "Montserrat", sans-serif;
    position: relative;
  }
  .card {
    position: absolute;
    width: 620px;
    height: 354px;
    border-radius: 18px;
    overflow: hidden;
    background: radial-gradient(ellipse at 50% 35%, var(--card-black-light), var(--card-black) 75%);
  }
  .card--back { left: 70px; top: 90px; }
  .card--front { left: 510px; top: 510px; }

  .brand-name {
    font-family: "Montserrat", sans-serif;
    font-weight: 700;
    color: var(--brand-red);
    text-transform: uppercase;
    line-height: 1.1;
    display: flex;
    align-items: center;
    gap: 12px;
  }
  .brand-name__mark {
    width: 16px; height: 16px;
    background: var(--brand-red);
    flex: none;
  }

  /* back */
  .card--back .brand-name {
    position: absolute;
    left: 0; right: 0; top: 104px;
    justify-content: center;
    font-size: 32px;
    letter-spacing: 1px;
  }
  .tagline {
    position: absolute;
    left: 0; right: 0; top: 162px;
    text-align: center;
    font-size: 15px;
    font-weight: 600;
    letter-spacing: 1px;
    color: var(--brand-yellow);
  }
  .card--back .web {
    position: absolute;
    left: 0; right: 0; top: 232px;
    text-align: center;
    font-size: 13px;
    letter-spacing: 4px;
    color: var(--white);
  }
  .web__accent { color: var(--brand-red); }
  .safety-strip {
    position: absolute;
    left: 0; right: 0; bottom: 0;
    height: 12px;
    background: repeating-linear-gradient(135deg, var(--brand-yellow) 0 14px, var(--card-black) 14px 28px);
  }

  /* front */
  .card__shapes { position: absolute; inset: 0; }
  .card--front .brand-name {
    position: absolute;
    left: 34px; top: 40px;
    width: 300px;
    font-size: 22px;
  }
  .person {
    position: absolute;
    right: 180px; top: 118px;
    text-align: right;
  }
  .person__name {
    font-family: "Oswald", sans-serif;
    font-weight: 500;
    font-size: 24px;
    color: var(--brand-red);
    text-transform: uppercase;
    letter-spacing: .5px;
    line-height: 1.2;
  }
  .person__title { font-size: 15px; color: var(--white); }

  .address {
    position: absolute;
    left: 150px; top: 200px;
    font-size: 13px;
    line-height: 1.35;
    color: var(--text-grey);
    font-style: normal;
  }
  .contact {
    position: absolute;
    left: 150px; top: 270px;
    list-style: none;
    font-size: 13px;
    line-height: 1.5;
    color: var(--text-grey);
  }
  .contact li { display: flex; align-items: center; gap: 8px; }
  .contact svg { width: 11px; height: 11px; fill: var(--brand-red); flex: none; }
</style>
</head>
<body>

<section class="card card--back">
  <div class="brand-name"><span class="brand-name__mark"></span>Norvane Builders Limited</div>
  <p class="tagline">Quality Starts from the Ground Up</p>
  <p class="web"><span class="web__accent">www.</span>norvanebuilders-example<span class="web__accent">.com</span></p>
  <div class="safety-strip" aria-hidden="true"></div>
</section>

<section class="card card--front">
  <svg class="card__shapes" viewBox="0 0 620 354" preserveAspectRatio="none" aria-hidden="true">
    <path d="M380 0 H620 V354 H560 C600 220 540 60 380 0 Z" fill="var(--brand-red)"/>
    <path d="M470 60 C560 130 585 250 560 354 H505 C560 230 540 130 470 60 Z" fill="var(--brand-yellow)"/>
  </svg>

  <div class="brand-name"><span class="brand-name__mark"></span>Norvane Builders Limited</div>

  <div class="person">
    <p class="person__name">Daniel Hartwell</p>
    <p class="person__title">President</p>
  </div>

  <address class="address">
    Norvane Builders Limited<br>
    42 Brenton Street<br>
    Elk Harbour, NL B3K 7T2
  </address>

  <ul class="contact">
    <li><svg viewBox="0 0 24 24"><path d="M6.6 10.8a15.1 15.1 0 0 0 6.6 6.6l2.2-2.2a1 1 0 0 1 1-.25 11.4 11.4 0 0 0 3.6.57 1 1 0 0 1 1 1V20a1 1 0 0 1-1 1A17 17 0 0 1 3 4a1 1 0 0 1 1-1h3.5a1 1 0 0 1 1 1c0 1.25.2 2.45.57 3.57a1 1 0 0 1-.25 1z"/></svg>709-555-0147</li>
    <li><svg viewBox="0 0 24 24"><path d="M6 2h12v6H6z M3 9h18v9h-3v4H6v-4H3z M8 15v5h8v-5z"/></svg>709-555-0192</li>
    <li><svg viewBox="0 0 24 24"><circle cx="12" cy="12" r="10"/></svg>www.norvanebuilders-example.com</li>
  </ul>
</section>

</body>
</html>
```